Life Coach for Lawyers Business Card Design

Elegant, original, business card design for life coaching service for associate attorneys who work in big law and struggle with stress, overwhelm, and time management. Double sided design.

Target Market(s)

Women associate attorneys who work in big law and struggle with stress, overwhelm, and time management.

Industry/Entity Type

Life Coaching

Contact Information for Business Card

Marissa Pendrell
Life Coach
518.677.3941
calmbriefcounsel.net
marissa@calmbriefcounsel.net
@calmbriefcounsel (Instagram)

Font styles to use
Other font styles liked:
• Silver South font duo. See uploaded files.

Requirements
Must have
• Icons for phone, website, email, and Instagram instead of words. Specific colors used in my logo (171B2B, 421121, FFFFFF)
Nice to have
• Foil. Embossed. Feminine design.
Should not have
• Any colors other than those used in logo. See uploaded files.

```html
<!DOCTYPE html>
<html lang="en">
<head>
<meta charset="utf-8">
<title>Calm Brief Counsel – Business Card</title>
<link rel="stylesheet" href="https://fonts.googleapis.com/css2?family=Playfair+Display:wght@400&family=Tinos:wght@400&display=swap">
<style>
  :root {
    --navy: #171B2B;
    --plum: #421121;
    --white: #FFFFFF;
    --gold-light: #F1DDB0;
    --gold: #C9A45C;
    --gold-deep: #A9823E;
    --backdrop: #EDEAE6;
  }
  * { box-sizing: border-box; margin: 0; padding: 0; }
  html, body {
    width: 1200px; height: 1200px; overflow: hidden;
    background: var(--backdrop);
  }
  .canvas { position: relative; width: 1200px; height: 1200px; }
  .card {
    position: absolute; left: 250px; width: 700px; height: 400px;
    box-shadow: 0 8px 24px rgba(23, 27, 43, 0.18);
    overflow: hidden;
  }

  /* Front */
  .card-front { top: 165px; background: var(--plum); }
  .front-brand {
    position: absolute; left: 0; right: 0; top: 150px;
    text-align: center;
    font-family: "Playfair Display", serif;
    font-weight: 400; font-size: 54px; letter-spacing: 1px;
    color: var(--white);
  }
  .foil-band {
    position: absolute; left: 190px; bottom: 0; width: 420px; height: 38px;
    border-radius: 18px 18px 0 0;
    background: linear-gradient(90deg, var(--gold-deep), var(--gold-light) 55%, var(--gold));
  }

  /* Back */
  .card-back { top: 635px; background: var(--white); }
  .holder {
    position: absolute; right: 40px; top: 34px; text-align: right;
    font-family: "Tinos", serif; color: var(--navy);
  }
  .holder-name { font-size: 52px; line-height: 1; font-weight: 400; }
  .holder-title { font-size: 16px; margin-top: 4px; }

  .brand-mark {
    position: absolute; left: 55px; top: 145px; width: 220px; height: 220px;
    border: 2px solid var(--gold); border-radius: 50%;
    display: flex; align-items: center; justify-content: center;
    text-align: center;
    font-family: "Playfair Display", serif; font-weight: 400;
    font-size: 26px; line-height: 1.2; color: var(--gold);
  }
  .divider {
    position: absolute; left: 340px; top: 165px; width: 2px; height: 215px;
    background: var(--plum);
  }
  .contacts {
    position: absolute; left: 362px; top: 182px; list-style: none;
    font-family: "Tinos", serif; font-size: 18px; color: var(--navy);
  }
  .contact-item {
    display: flex; align-items: center; gap: 12px;
    height: 26px; margin-bottom: 22px; white-space: nowrap;
  }
  .contact-icon { flex: none; width: 24px; height: 24px; }
</style>
</head>
<body>
<main class="canvas">
  <section class="card card-front" aria-label="Card front">
    <p class="front-brand">Calm Brief Counsel</p>
    <div class="foil-band"></div>
  </section>

  <section class="card card-back" aria-label="Card back">
    <header class="holder">
      <h1 class="holder-name">Marissa Pendrell</h1>
      <p class="holder-title">Life Coach</p>
    </header>

    <div class="brand-mark">Calm Brief<br>Counsel</div>
    <div class="divider"></div>

    <ul class="contacts">
      <li class="contact-item">
        <svg class="contact-icon" viewBox="0 0 24 24" aria-label="Phone">
          <rect width="24" height="24" rx="3" fill="#421121"/>
          <path d="M8 5.5 L10 5.5 L11 9 L9.5 10.3 Q11 13.5 13.7 14.5 L15 13 L18.5 14 L18.5 16 Q18.5 18.5 16 18.5 Q7 17.5 5.5 8 Q5.5 5.5 8 5.5 Z" fill="#FFFFFF"/>
        </svg>
        518.677.3941
      </li>
      <li class="contact-item">
        <svg class="contact-icon" viewBox="0 0 24 24" aria-label="Website">
          <rect width="24" height="24" rx="3" fill="#421121"/>
          <g fill="none" stroke="#FFFFFF" stroke-width="1.3">
            <circle cx="12" cy="12" r="7"/>
            <ellipse cx="12" cy="12" rx="3" ry="7"/>
            <path d="M5 12 H19 M6.2 8.5 H17.8 M6.2 15.5 H17.8"/>
          </g>
        </svg>
        calmbriefcounsel.net
      </li>
      <li class="contact-item">
        <svg class="contact-icon" viewBox="0 0 24 24" aria-label="Email">
          <rect width="24" height="24" rx="3" fill="#421121"/>
          <rect x="5" y="7" width="14" height="10" fill="none" stroke="#FFFFFF" stroke-width="1.3"/>
          <path d="M5 7 L12 12.5 L19 7" fill="none" stroke="#FFFFFF" stroke-width="1.3"/>
        </svg>
        marissa@calmbriefcounsel.net
      </li>
      <li class="contact-item">
        <svg class="contact-icon" viewBox="0 0 24 24" aria-label="Social handle">
          <circle cx="12" cy="12" r="11" fill="#421121"/>
        </svg>
        @calmbriefcounsel
      </li>
    </ul>
  </section>
</main>
</body>
</html>
```